Australian small vineyard seeking wine label.

We need a wine label design for a new wine brand \Boutique winery - 2 vintages so far, looking for something a little eye catching, but simple.
Wine label name: Harlow and Co
2013 Cabernet Shiraz
2014 Shiraz
Estate grown
Vineyard located at Sevenhill in the Clare valley South Australia.

Target Market(s)

ladies aged between 20 and 50

Industry/Entity Type

Boutique

Logo Text

Harlow and Co

Logo styles of interest
Emblem Logo
Pictorial/Combination Logo
Abstract Logo
Character Logo
Font styles to use
Serif
Script

Requirements
Must have
• easy to read text
Nice to have
• The grape grower and winemaker is Martin Harlow -
• had some thoughts of Captain Brindle - Australian - naval flag
• But very open to ideas
Should not have
• over complications and colors due to cost of wine label being determined by amount of colors required abd print set up.

```html
<!DOCTYPE html>
<html lang="en">
<head>
<meta charset="utf-8">
<title>Harlow &amp; Co — Cabernet Shiraz Label</title>
<link rel="stylesheet" href="https://fonts.googleapis.com/css2?family=Cinzel:wght@400;500;600&family=Cormorant+Garamond:ital,wght@1,600&family=Questrial&display=swap">
<style>
  :root {
    --wine: #5a2e31;
    --wine-deep: #4e2629;
    --paper: #eeebe6;
    --stock: #ebe8e3;
    --vine-light: #ad9b8c;
    --vine-dark: #6e4043;
    --rule: #8a3a2e;
    --page: #ffffff;
  }
  * { margin: 0; padding: 0; box-sizing: border-box; }
  html, body {
    width: 1040px; height: 1200px; overflow: hidden;
    background: var(--page);
  }
  .canvas { position: relative; width: 1040px; height: 1200px; }

  .label-stock {
    position: absolute; left: 158px; top: 118px; width: 724px; height: 964px;
    background: var(--stock); border-radius: 34px;
  }
  .label-frame {
    position: absolute; left: 197px; top: 157px; width: 646px; height: 886px;
    background: var(--wine); border-radius: 38px;
  }
  .label-panel {
    position: absolute; left: 206px; top: 166px; width: 628px; height: 637px;
    background: var(--paper); border-radius: 32px;
  }

  .country {
    position: absolute; left: 0; width: 1040px; top: 204px;
    text-align: center; font-family: "Cinzel", serif; font-weight: 500;
    font-size: 34px; letter-spacing: 1px; color: var(--wine);
  }
  .brand-name {
    position: absolute; left: 0; width: 1040px; top: 262px;
    text-align: center; font-family: "Questrial", sans-serif;
    font-size: 92px; line-height: 1; color: var(--wine);
  }
  .brand-rule {
    position: absolute; left: 240px; top: 371px; width: 560px; height: 2px;
    background: var(--wine);
  }

  .vine-artwork {
    position: absolute; left: 356px; top: 412px; width: 328px; height: 256px;
    border-radius: 40% 40% 46% 46%;
    background: radial-gradient(ellipse at 50% 40%, var(--vine-light) 0%, #c3b4a7 55%, rgba(238,235,230,0) 75%);
  }
  .vine-artwork::after {
    content: ""; position: absolute; left: 110px; top: 100px; width: 110px; height: 150px;
    border-radius: 50% 50% 50% 50% / 40% 40% 60% 60%;
    background: radial-gradient(ellipse at 50% 40%, var(--vine-dark) 0%, rgba(110,64,67,0.25) 70%, rgba(110,64,67,0) 100%);
  }

  .estate-rule {
    position: absolute; left: 330px; width: 390px; height: 1px; background: var(--rule);
  }
  .estate-rule.top { top: 698px; }
  .estate-rule.bottom { top: 766px; }
  .estate {
    position: absolute; left: 0; width: 1040px; top: 714px;
    text-align: center; font-family: "Cinzel", serif; font-weight: 500;
    font-size: 29px; letter-spacing: 4px; color: var(--wine);
  }

  .vintage {
    position: absolute; left: 0; width: 1040px; top: 822px;
    text-align: center; font-family: "Cormorant Garamond", serif; font-style: italic;
    font-weight: 600; font-size: 50px; font-variant: small-caps; color: var(--paper);
  }
  .varietal {
    position: absolute; left: 0; width: 1040px; top: 890px;
    text-align: center; font-family: "Cinzel", serif; font-weight: 400;
    font-size: 46px; letter-spacing: 1px; color: var(--paper);
  }
  .region {
    position: absolute; left: 0; width: 1040px; top: 964px;
    text-align: center; font-family: "Cinzel", serif; font-weight: 600;
    font-size: 20px; line-height: 27px; color: var(--paper);
  }
</style>
</head>
<body>
  <div class="canvas">
    <div class="label-stock"></div>
    <div class="label-frame"></div>
    <div class="label-panel"></div>

    <div class="country">Australia</div>
    <div class="brand-name">Harlow &amp; Co</div>
    <div class="brand-rule"></div>

    <div class="vine-artwork" role="img" aria-label="Engraved illustration of grape vine leaves with three hanging grape bunches"></div>

    <div class="estate-rule top"></div>
    <div class="estate">Estate Grown</div>
    <div class="estate-rule bottom"></div>

    <div class="vintage">Vintage 2013</div>
    <div class="varietal">Cabernet Shiraz</div>
    <div class="region">Sevenhill - Clare Valley<br>South Australia</div>
  </div>
</body>
</html>
```